Powerpoint design template for FLOMBIRT for new digital platform

We would like to use a PowerPoint template, we would like to create a new page, we would like to create a new digital platform FLOMBIRT for schools and parents for the creation of playful communication and educational tools for children to enhance their positive development, amaze them learn in a playful way. This platform is going to be the most creative, stimulating and innovative classroom, easy to use and fast to implement. Scrapbooking, collages ... Magazine, newsletters Diplomla / awards Slideshows Facebook Calendars Organizers Greetings Games ... This powerpoint template will be used essential to We are looking for a professional design, positioning our brand in the children market with an adult hearing. so you will need to find a good deal. Primary target: nurseries & schools from 0 to 18 years old and universities (in 2nd phase) Secondary target: small & medium businesses Third target: general public, and TPE If it is a color scheme, then it is suggested that it be marketed in Europe (UK, Italy, Spain) and in a 2nd Stage USA and other countries. multiple options for front page, insidious pages (multiple styles with limited text and extended text) and final contact page We need something to read, we can not do it too much, but we can not do it. , and inside pages aligned to our logo

Target Market(s)

Target 1; Education with teacher Target 2; parents and grandparents

Industry/Entity Type

Education

Font styles to use
Other font styles liked:
• not decided. but not too fancy

Requirements
Must have
• Multi page options for front page, page insides (multiple styles with limited text and extended text) and final page contact
Nice to have
• do not have a lot of ideas. We need something to read, we can not get away from it
Should not have
• not too fancy and busy: keep clarity & simplicity while reassuring on quality

```html
<!DOCTYPE html>
<html lang="en">
<head>
<meta charset="utf-8">
<title>FLOMBIRT – Inside Page</title>
<link href="https://fonts.googleapis.com/css2?family=Open+Sans:wght@400;600;700&display=swap" rel="stylesheet">
<style>
  :root {
    --paper: #ffffff;
    --cream: #fdf7c4;
    --rule: #b3412c;
    --ink: #45474a;
    --orange: #f5a81c;
    --pink: #e6287a;
    --teal: #4b8b96;
    --violet: #8e63b5;
    --brand: #2b2b2b;
    --lime: #c6d92e;
    --art-a: #f7d3a4;
    --art-b: #eea46f;
    --art-c: #f3c9b8;
  }
  * { margin: 0; padding: 0; box-sizing: border-box; }
  html, body { width: 1200px; height: 900px; overflow: hidden; }
  body { font-family: "Open Sans", Arial, sans-serif; background: var(--paper); }

  .slide { position: relative; width: 1200px; height: 900px; background: var(--paper); overflow: hidden; }

  .brand { position: absolute; top: 30px; right: 40px; display: flex; flex-direction: column; align-items: flex-start; }
  .brand-row { display: flex; align-items: center; gap: 10px; }
  .brand-mark { width: 22px; height: 22px; background: var(--lime); }
  .brand-name { font-weight: 700; font-size: 38px; letter-spacing: 1px; color: var(--brand); line-height: 1; }
  .brand-tagline { margin-top: 6px; margin-left: 32px; font-size: 10px; line-height: 1.2; letter-spacing: 1px; text-transform: uppercase; color: var(--brand); }

  .hero-art {
    position: absolute; left: 0; top: 120px; width: 1200px; height: 240px;
    background: linear-gradient(90deg, var(--art-a) 0%, var(--art-b) 35%, var(--art-c) 60%, var(--art-b) 85%, var(--art-a) 100%);
    opacity: 0.75;
  }

  .content-area { position: absolute; left: 0; top: 360px; width: 1200px; height: 540px; background: var(--cream); border-top: 6px solid var(--rule); }

  .topic { position: absolute; left: 52px; width: 1100px; }
  .topic-1 { top: 446px; }
  .topic-2 { top: 593px; }
  .topic-3 { top: 731px; }

  .topic-icon { position: absolute; left: 0; top: 16px; width: 50px; height: 62px; }
  .topic-title { margin-left: 100px; font-weight: 600; font-size: 29px; line-height: 38px; }
  .topic-1 .topic-title { color: var(--orange); }
  .topic-2 .topic-title { color: var(--pink); }
  .topic-3 .topic-title { color: var(--teal); }
  .topic-text { margin-left: 100px; font-size: 24.5px; line-height: 36px; color: var(--ink); }
</style>
</head>
<body>
<main class="slide">
  <div class="brand">
    <div class="brand-row">
      <span class="brand-mark"></span>
      <span class="brand-name">FLOMBIRT</span>
    </div>
    <p class="brand-tagline">Your tagline<br>goes here</p>
  </div>

  <div class="hero-art" role="img" aria-label="Illustration of five cheerful cartoon children leaning over the edge of the page holding books, an apple and a pencil"></div>

  <section class="content-area"></section>

  <article class="topic topic-1">
    <svg class="topic-icon" viewBox="0 0 50 62" aria-hidden="true">
      <rect x="8" y="4" width="34" height="50" rx="3" fill="var(--violet)" transform="rotate(-14 25 31)"/>
    </svg>
    <h2 class="topic-title">Subtext here</h2>
    <p class="topic-text">Lemon drops oat cake oat cake sugar plum sweet gingerbread chocolate<br>cake gingerbread. Lemon drops oat cake oat cake sugar plum sweet</p>
  </article>

  <article class="topic topic-2">
    <svg class="topic-icon" viewBox="0 0 50 62" aria-hidden="true">
      <rect x="8" y="4" width="34" height="50" rx="3" fill="var(--pink)" transform="rotate(-14 25 31)"/>
    </svg>
    <h2 class="topic-title">Subtext here</h2>
    <p class="topic-text">Lemon drops oat cake oat cake sugar plum sweet gingerbread chocolate<br>cake gingerbread. Lemon drops oat cake oat cake sugar plum sweet</p>
  </article>

  <article class="topic topic-3">
    <svg class="topic-icon" viewBox="0 0 50 62" aria-hidden="true">
      <rect x="8" y="4" width="34" height="50" rx="3" fill="var(--teal)" transform="rotate(-14 25 31)"/>
    </svg>
    <h2 class="topic-title">Subtext here</h2>
    <p class="topic-text">Lemon drops oat cake oat cake sugar plum sweet gingerbread chocolate<br>cake gingerbread. Lemon drops oat cake oat cake sugar plum sweet</p>
  </article>
</main>
</body>
</html>
```